Business cards and stationary for a machine shop
K7 Lathe, LLC
Professional
(see below)
48B Garnet Avenue
Hollisford, MA 01999
dumont@k7lathe-example.com
www.k7lathe-example.com
On the bottom left to be the address, website and phone number
On the bottom right to be both names and cell numbers
Roy Dumont (508)555-0143
Gwen Dumont (508)555-0187
I like the look of this one. I don't know if you can turn it around to be a "P"
This is the AI file of my logo

```html
<!DOCTYPE html>
<html lang="en">
<head>
<meta charset="utf-8">
<title>K7 Lathe, LLC — Business Card</title>
<link href="https://fonts.googleapis.com/css2?family=Montserrat:wght@400;600;700&display=swap" rel="stylesheet">
<style>
  :root {
    --bg: #e9e7e4;
    --black: #0c0c0c;
    --black-soft: #1c1c1c;
    --red: #d0151b;
    --red-deep: #7e080c;
    --white: #ffffff;
    --grey: #8a8a8a;
    --grey-faint: #3a3a3a;
  }
  * { margin: 0; padding: 0; box-sizing: border-box; }
  html, body { width: 1200px; height: 629px; overflow: hidden; }
  body {
    background: var(--bg);
    font-family: "Montserrat", Arial, sans-serif;
    position: relative;
  }
  .card {
    position: absolute;
    top: 166px;
    width: 520px;
    height: 297px;
    border-radius: 6px;
    overflow: hidden;
    box-shadow: 0 8px 24px rgba(0,0,0,.18);
  }
  .card-back {
    left: 50px;
    background: radial-gradient(ellipse at 50% 35%, var(--black-soft), var(--black) 70%);
    display: flex;
    flex-direction: column;
    align-items: center;
    justify-content: center;
    gap: 22px;
  }
  .back-mark { display: flex; align-items: center; gap: 14px; }
  .back-mark .dot { width: 30px; height: 30px; border-radius: 50%; background: var(--red); }
  .back-mark .name { font-size: 46px; font-weight: 700; color: var(--grey-faint); letter-spacing: 2px; }
  .back-web { font-size: 12px; letter-spacing: 3px; color: var(--grey); }
  .card-front { left: 630px; background: var(--black); }
  .front-top {
    height: 150px;
    background: linear-gradient(180deg, var(--black-soft), var(--black));
    display: flex;
    flex-direction: column;
    align-items: center;
    justify-content: center;
    gap: 8px;
  }
  .logo { display: flex; align-items: center; gap: 12px; }
  .logo .dot { width: 22px; height: 22px; border-radius: 50%; background: var(--red); }
  .logo .name { font-size: 30px; font-weight: 700; color: var(--white); letter-spacing: 1px; }
  .tagline { font-size: 9px; font-weight: 600; color: var(--red); letter-spacing: 2px; text-transform: uppercase; }
  .divider { height: 6px; background: var(--black-soft); border-top: 1px solid #333; }
  .front-bottom {
    height: 141px;
    background: linear-gradient(180deg, var(--red), var(--red-deep));
    display: flex;
    justify-content: space-between;
    padding: 22px 26px;
    color: var(--white);
    font-size: 11.5px;
    line-height: 1.55;
  }
  .people .person { margin-bottom: 10px; }
  .people .person strong { font-weight: 600; display: block; }
  .contact-list { list-style: none; }
  .contact-list li { display: flex; align-items: center; gap: 8px; }
  .contact-list svg { width: 13px; height: 13px; flex: none; }
</style>
</head>
<body>

<section class="card card-back" aria-label="Card back">
  <div class="back-mark">
    <span class="dot"></span>
    <span class="name">K7 Lathe</span>
  </div>
  <p class="back-web">www.k7lathe-example.com</p>
</section>

<section class="card card-front" aria-label="Card front">
  <div class="front-top">
    <div class="logo">
      <span class="dot"></span>
      <span class="name">K7 Lathe, LLC</span>
    </div>
    <p class="tagline">Precision Machining Services</p>
  </div>
  <div class="divider"></div>
  <div class="front-bottom">
    <div class="people">
      <div class="person"><strong>Roy Dumont</strong>(508)555-0143</div>
      <div class="person"><strong>Gwen Dumont</strong>(508)555-0187</div>
    </div>
    <ul class="contact-list">
      <li>
        <svg viewBox="0 0 16 16"><path d="M8 1a5 5 0 0 0-5 5c0 4 5 9 5 9s5-5 5-9a5 5 0 0 0-5-5zm0 7a2 2 0 1 1 0-4 2 2 0 0 1 0 4z" fill="#fff"/></svg>
        48B Garnet Avenue
      </li>
      <li>
        <svg viewBox="0 0 16 16"></svg>
        Hollisford, MA 01999
      </li>
      <li>
        <svg viewBox="0 0 16 16"><path d="M4 1h3l1 4-2 1a9 9 0 0 0 4 4l1-2 4 1v3c0 1-1 2-2 2C7 14 2 9 2 3c0-1 1-2 2-2z" fill="#fff"/></svg>
        (508)555-0143
      </li>
      <li>
        <svg viewBox="0 0 16 16"><rect x="1" y="3" width="14" height="10" rx="1" fill="none" stroke="#fff" stroke-width="1.5"/><path d="M1 4l7 5 7-5" fill="none" stroke="#fff" stroke-width="1.5"/></svg>
        dumont@k7lathe-example.com
      </li>
      <li>
        <svg viewBox="0 0 16 16"><circle cx="8" cy="8" r="6.5" fill="none" stroke="#fff" stroke-width="1.3"/><path d="M1.5 8h13M8 1.5c-3 3-3 10 0 13M8 1.5c3 3 3 10 0 13" fill="none" stroke="#fff" stroke-width="1.1"/></svg>
        www.k7lathe-example.com
      </li>
    </ul>
  </div>
</section>

</body>
</html>
```